Plakat-Design für eine große Anschlagfläche
Zielgruppe
Geräte Hafen ist ein Forum über Technik (Smart Home, HiFi, Smartphones, usw.) welches Nutzern die Möglichkeit bietet, sich über Technik auszutauschen.
Durch die Aktivität des Nutzers bekommt dieser Punkte gutgeschrieben.
Mit diesen Punkten kann man Tickets kaufen, womit man an einer Verlosung von technischen Geräten teilnimmt (z.B. Headsets, Smartphones, Konsolen, ...)
Die Zielgruppe sind Technik Interessierte.
Aufgabenstellung
Es soll deutlich werden, dass es sich um ein Forum handelt, welches sich auf Technik spezialisiert. Folgende Oberbegriffe werden in dem Forum behandelt:
Unterhaltungselektronik, Smart Home, Smartphone & Handys, Foto & Camcorder, Computer, PC-Komponenten, Gaming und Konsolen, Kfz & eMobility, Haushalts- und Gartengeräte und Körper und Fittness
Dem Nutzer wird also die Möglichkeit geboten, sich mit anderen Technikinteressierten auszutauschen.
Durch die Aktivität im Forum bekommt man Punkte, womit man Tickets für Verlosungen kaufen kann und somit eine Chance auf den Gewinn hat. Geräte Hafen selber verlost regelmäßig Technikgegenstände wie Headsets, Smartphones, Konsolen, ...
Die Nutzer werden also durch Punkte belohnt, die zu einem Sachgewinn führen können. Dies muss erwähnt werden, damit Leser des Plakats sehen, dass es sich dort lohnt aktiv zu werden.
Sonstige Sachen die erwähnt werden können:
- modernes Forum, welches einen super Überblick über alles liefert
- nette und freundliche Community
Ich hoffe auf ihre Kreativität, für weitere Dinge.
Kurz gesagt: Es ist ein Forum mit der Chance auf Sachgewinne bei Aktivität.
Die Gewichtung der Erwähnung mit den Chance auf Sachgewinne, sollte unter 50% liegen. Es soll also nicht das ganze Plakat voll damit sein.
Das Forum an sich soll auch gut beworben werden, wenn es jetzt z.B. nicht sowas wie Gewinne geben würde.
Maße und weiteres:
Format: 59cm x 41cm (B x H)
Auflösung: min. 150 dpi
Farbraum: CMYK
Ich hänge ein Logo in den Anhang, woran sich orientiert werden soll (Farben) und welches mit eingebunden werden muss.

```html
<!DOCTYPE html>
<html lang="de">
<head>
<meta charset="utf-8">
<title>Geräte Hafen – Let's talk about technic</title>
<link rel="stylesheet" href="https://fonts.googleapis.com/css2?family=Exo+2:wght@500&family=Barlow:wght@500;600&display=swap">
<style>
  :root {
    --brand-blue: #1d5aa6;
    --ink-grey: #5a6677;
    --sub-grey: #6e7884;
    --cloud-light: rgba(246, 248, 251, 0.95);
    --cloud-shade: rgba(196, 206, 218, 0.55);
    --bg-top: #dde6ee;
    --bg-mid: #c8d6e2;
    --bg-low: #e9eef3;
    --cta-red: #b3120f;
    --white: #ffffff;
  }
  html, body { margin: 0; padding: 0; overflow: hidden; }
  body { width: 1200px; height: 834px; }
  .poster {
    position: relative;
    width: 1200px;
    height: 834px;
    overflow: hidden;
    background: linear-gradient(180deg, var(--bg-top) 0%, var(--bg-mid) 55%, var(--bg-low) 100%);
    font-family: "Barlow", Arial, sans-serif;
  }
  .backdrop-circuit {
    position: absolute; inset: 0;
    background: radial-gradient(ellipse at 60% 40%, rgba(255,255,255,0.45), rgba(255,255,255,0) 65%);
  }
  .headline {
    position: absolute; left: 0; right: 0; top: 22px;
    margin: 0; text-align: center;
    font-family: "Exo 2", Arial, sans-serif; font-weight: 500;
    font-size: 92px; letter-spacing: 1px; line-height: 1.1; color: var(--brand-blue);
  }
  .tagline {
    position: absolute; left: 0; right: 0; top: 122px;
    margin: 0; text-align: center;
    font-size: 27px; font-weight: 500; letter-spacing: 1px; color: var(--sub-grey);
  }
  .topic-cloud-area {
    position: absolute; left: 150px; top: 185px; width: 920px; height: 430px;
    border-radius: 50%;
    background: radial-gradient(ellipse at 50% 45%, var(--cloud-light) 0%, var(--cloud-shade) 60%, rgba(196,206,218,0) 100%);
  }
  .topic-labels { position: absolute; left: 0; top: 0; }
  .topic-labels text {
    font-family: "Barlow", Arial, sans-serif; font-weight: 600;
    fill: var(--ink-grey); text-anchor: middle; letter-spacing: 1px;
  }
  .prize-callout {
    position: absolute; left: 0; top: 605px;
    width: 440px; height: 180px; padding: 22px 0 0 28px; box-sizing: border-box;
    background: var(--cta-red); border-radius: 0 10px 10px 0;
    color: var(--white); font-size: 35px; font-weight: 600; line-height: 1.2;
    letter-spacing: 0.5px;
  }
  .brand-mark {
    position: absolute; left: 804px; top: 608px; width: 360px; text-align: center;
  }
  .brand-dot {
    width: 110px; height: 110px; margin: 0 auto 12px;
    border-radius: 50%; background: var(--brand-blue);
  }
  .brand-name {
    margin: 0; font-size: 44px; font-weight: 500; letter-spacing: 2px;
    color: var(--brand-blue); line-height: 1;
  }
  .brand-url {
    margin: 10px 0 0; font-size: 23px; font-weight: 500;
    letter-spacing: 1px; color: var(--sub-grey);
  }
</style>
</head>
<body>
<main class="poster">
  <div class="backdrop-circuit" role="img" aria-label="Heller Hintergrund mit feinem Platinen-Leiterbahnmuster"></div>

  <h1 class="headline">Let's talk about technic</h1>
  <p class="tagline">Die moderne &amp; freundliche Community</p>

  <div class="topic-cloud-area" role="img" aria-label="Wolke aus hellgrauen Sprechblasen mit den Forenthemen"></div>

  <svg class="topic-labels" width="1200" height="834" viewBox="0 0 1200 834" aria-label="Forenthemen">
    <text x="336" y="268" font-size="26">PC-</text>
    <text x="336" y="298" font-size="26">Komponenten</text>
    <text x="566" y="244" font-size="32">Unterhaltungs-</text>
    <text x="566" y="282" font-size="32">elektronik</text>
    <text x="783" y="305" font-size="38">Kfz &amp;</text>
    <text x="783" y="347" font-size="38">eMobility</text>
    <text x="905" y="399" font-size="38">HiFi</text>
    <text x="278" y="360" font-size="31">Smart</text>
    <text x="278" y="394" font-size="31">Home</text>
    <text x="521" y="387" font-size="41">Smartphone &amp;</text>
    <text x="521" y="432" font-size="41">Handys</text>
    <text x="746" y="465" font-size="37">Computer</text>
    <text x="232" y="492" font-size="36">Head-</text>
    <text x="232" y="532" font-size="36">sets</text>
    <text x="389" y="492" font-size="36">Gaming &amp;</text>
    <text x="389" y="532" font-size="36">Konsolen</text>
    <text x="558" y="540" font-size="21">Haushalts- &amp;</text>
    <text x="558" y="566" font-size="21">Gartengeräte</text>
    <text x="714" y="519" font-size="27">Körper &amp;</text>
    <text x="714" y="549" font-size="27">Fitness</text>
    <text x="919" y="501" font-size="37">Foto &amp;</text>
    <text x="919" y="540" font-size="37">Camcorder</text>
  </svg>

  <div class="prize-callout">Mitreden, Punkte<br>sammeln und coole<br>Preise gewinnen!</div>

  <div class="brand-mark">
    <div class="brand-dot"></div>
    <p class="brand-name">GERÄTE HAFEN</p>
    <p class="brand-url">www.geraete-hafen.com</p>
  </div>
</main>
</body>
</html>
```